jQuery Mobile CSS for web app

Task Outline:
Create jQuery Mobile themeroller compliant CSS and icons for a mobile web app.
Task Description:
Corvel Dynamics are in the process of implementing a new, web based version of their Meridex operations platform.
The web based version of Meridex is built on top of the jQuery Mobile platform and we are looking for a designer to create a jQuery Mobile themeroller compliant CSS theme pack that we can plug into our application. The aim is to remove the standard jQuery Mobile look and feel and to introduce the Corvel branding throughout the new web app.
A number of screenshots are shown in the attached design spec (corvel_dynamics.pdf) that show what the current (Windows Mobile 6.5) application looks like, alongside the development version of our new web app.
Deliverables:
• jQuery Mobile (v 1.4.2) themeroller compliant CSS which provides theming for all jQuery Mobile UI components.
• Example html showing how to use the CSS theme (especially where additional html/css classes are required).
• New set of status icons (as listed in attachment)
Inspiration:
See our website for current branding: www.corvel-dynamics-web.com

```html
<!DOCTYPE html>
<html lang="en">
<head>
<meta charset="utf-8">
<title>Varnoth Kelmira</title>
<link rel="stylesheet" href="https://fonts.googleapis.com/css2?family=Roboto:wght@400;500&display=swap">
<style>
  :root {
    --header-bg: #000000;
    --screen-bg: #2f2f2f;
    --screen-bg-light: #353535;
    --text: #ffffff;
    --face-top: #fbfbfb;
    --face-bottom: #e6e6e6;
    --menu-bg: #7d7d7d;
    --menu-icon: #2a3850;
    --band-green: #9acb4d;
    --band-red: #e2363a;
    --band-blue: #5d86d4;
    --band-steel: #6e9dbf;
    --band-grey: #7e7c8a;
    --band-gold: #d0a50a;
    --icon-red: #cc1c22;
    --icon-green: #3f9b16;
    --icon-gold: #e0b70a;
  }
  * { box-sizing: border-box; margin: 0; padding: 0; }
  html, body { width: 795px; height: 1200px; overflow: hidden; }
  body {
    position: relative;
    font-family: "Roboto", Arial, sans-serif;
    color: var(--text);
    background: radial-gradient(ellipse at 50% 40%, var(--screen-bg-light), var(--screen-bg));
  }
  .app-header {
    position: absolute; left: 0; top: 0; width: 795px; height: 158px;
    background: var(--header-bg);
  }
  .app-title {
    position: absolute; left: 202px; top: 53px;
    font-size: 45px; font-weight: 400; line-height: 52px; letter-spacing: 0;
    white-space: nowrap;
  }
  .menu-button {
    position: absolute; left: 666px; top: 46px; width: 71px; height: 69px;
    border-radius: 6px; background: var(--menu-bg);
    box-shadow: inset 0 1px 0 rgba(255,255,255,0.25);
    display: flex; align-items: center; justify-content: center;
  }
  .tile {
    position: absolute; width: 206px; height: 208px; border-radius: 30px;
    box-shadow: 0 4px 8px rgba(0,0,0,0.45);
  }
  .tile::after {
    content: ""; position: absolute; inset: 0; border-radius: 30px;
    background: linear-gradient(90deg, rgba(0,0,0,0.15), rgba(255,255,255,0.18) 50%, rgba(0,0,0,0.15));
  }
  .tile-face {
    position: absolute; left: 0; top: 0; width: 100%; height: 162px; border-radius: 30px; z-index: 1;
    background: linear-gradient(180deg, var(--face-top), var(--face-bottom));
    display: flex; align-items: center; justify-content: center;
  }
  .band-green { background: var(--band-green); }
  .band-red { background: var(--band-red); }
  .band-blue { background: var(--band-blue); }
  .band-steel { background: var(--band-steel); }
  .band-grey { background: var(--band-grey); }
  .band-gold { background: var(--band-gold); }
  .person-figure {
    width: 110px; height: 124px; border-radius: 50px 50px 16px 16px;
    background: linear-gradient(180deg, #d98e55 0%, #c47a45 40%, #27405a 55%, #1d2f44 100%);
  }
  .tile-label {
    position: absolute; width: 240px; text-align: center;
    font-size: 37px; line-height: 44px; font-weight: 400;
  }
  .tile-label.compact { font-size: 33px; }
  .build-code { position: absolute; left: 709px; top: 1155px; font-size: 20px; }
</style>
</head>
<body>
  <header class="app-header">
    <h1 class="app-title">Varnoth Kelmira</h1>
    <div class="menu-button">
      <svg width="26" height="20" viewBox="0 0 26 20"><g fill="var(--menu-icon)"><rect y="1" width="26" height="3.5" rx="1"/><rect y="8" width="26" height="3.5" rx="1"/><rect y="15" width="26" height="3.5" rx="1"/></g></svg>
    </div>
  </header>

  <!-- Row 1 -->
  <div class="tile band-green" style="left:56px;top:232px">
    <div class="tile-face"><div class="person-figure" role="img" aria-label="Illustration of a person in a business suit"></div></div>
  </div>
  <div class="tile-label" style="left:38px;top:460px">My Work</div>

  <div class="tile band-red" style="left:297px;top:232px">
    <div class="tile-face">
      <svg width="130" height="130" viewBox="0 0 130 130">
        <line x1="72" y1="72" x2="118" y2="118" stroke="#c9c9c9" stroke-width="12" stroke-linecap="round"/>
        <line x1="72" y1="72" x2="84" y2="84" stroke="#8bc34a" stroke-width="12" stroke-linecap="round"/>
        <circle cx="46" cy="46" r="38" fill="#f3f6fa" stroke="#b8b8b8" stroke-width="7"/>
      </svg>
    </div>
  </div>
  <div class="tile-label" style="left:279px;top:460px">New Job<br>Order</div>

  <div class="tile band-blue" style="left:535px;top:232px">
    <div class="tile-face">
      <svg width="112" height="102" viewBox="0 0 112 102">
        <rect x="2" y="2" width="108" height="98" fill="#ffffff" stroke="#8a8a8a" stroke-width="3"/>
        <rect x="2" y="2" width="108" height="24" fill="#c8141c"/>
        <g stroke="#9a9a9a" stroke-width="2">
          <line x1="2" y1="44" x2="110" y2="44"/><line x1="2" y1="62" x2="110" y2="62"/><line x1="2" y1="80" x2="110" y2="80"/>
          <line x1="20" y1="26" x2="20" y2="100"/><line x1="38" y1="26" x2="38" y2="100"/><line x1="56" y1="26" x2="56" y2="100"/><line x1="74" y1="26" x2="74" y2="100"/><line x1="92" y1="26" x2="92" y2="100"/>
        </g>
      </svg>
    </div>
  </div>
  <div class="tile-label" style="left:518px;top:460px">Field</div>

  <!-- Row 2 -->
  <div class="tile band-blue" style="left:50px;top:568px">
    <div class="tile-face">
      <svg width="112" height="118" viewBox="0 0 112 118">
        <rect x="4" y="12" width="104" height="102" rx="8" fill="#c1321e" stroke="#8a1e10" stroke-width="2"/>
        <rect x="14" y="22" width="84" height="84" fill="#f7f7f7"/>
        <path d="M40 18 h32 v-6 a10 10 0 0 0 -32 0 z" fill="#e8e8e8" stroke="#8a8a8a" stroke-width="2"/>
      </svg>
    </div>
  </div>
  <div class="tile-label" style="left:36px;top:800px">Timesheet</div>

  <div class="tile band-steel" style="left:292px;top:568px">
    <div class="tile-face">
      <svg width="140" height="100" viewBox="0 0 140 100">
        <path d="M6 44 L24 30 L54 58 L116 4 L134 18 L54 94 Z" fill="#ffffff" stroke="var(--icon-red)" stroke-width="4" stroke-linejoin="round"/>
      </svg>
    </div>
  </div>
  <div class="tile-label compact" style="left:275px;top:800px">Authorisation</div>

  <div class="tile band-red" style="left:533px;top:568px">
    <div class="tile-face">
      <svg width="120" height="120" viewBox="0 0 120 120">
        <circle cx="60" cy="60" r="58" fill="var(--icon-gold)"/>
        <g fill="#111111">
          <path d="M60 60 L118 60 A58 58 0 0 0 89 9.8 Z"/>
          <path d="M60 60 L31 9.8 A58 58 0 0 0 2 60 Z"/>
          <path d="M60 60 L31 110.2 A58 58 0 0 0 89 110.2 Z"/>
        </g>
        <circle cx="60" cy="60" r="10" fill="#111111" stroke="var(--icon-gold)" stroke-width="5"/>
      </svg>
    </div>
  </div>
  <div class="tile-label" style="left:515px;top:800px">Asset</div>

  <!-- Row 3 -->
  <div class="tile band-grey" style="left:50px;top:876px">
    <div class="tile-face">
      <svg width="112" height="116" viewBox="0 0 112 116">
        <path d="M70 20 A44 44 0 1 1 26 34" fill="none" stroke="var(--icon-green)" stroke-width="12" stroke-linecap="round"/>
        <path d="M62 2 L96 18 L66 38 Z" fill="var(--icon-green)"/>
      </svg>
    </div>
  </div>
  <div class="tile-label" style="left:34px;top:1104px">Tag It</div>

  <div class="tile band-gold" style="left:292px;top:876px">
    <div class="tile-face">
      <svg width="120" height="110" viewBox="0 0 120 110">
        <ellipse cx="58" cy="46" rx="56" ry="42" fill="var(--icon-gold)"/>
        <path d="M84 78 L104 104 L70 86 Z" fill="var(--icon-gold)"/>
        <g fill="#ffffff"><circle cx="32" cy="46" r="8"/><circle cx="58" cy="46" r="8"/><circle cx="84" cy="46" r="8"/></g>
      </svg>
    </div>
  </div>
  <div class="tile-label" style="left:286px;top:1104px">Form Teat</div>

  <div class="build-code">C7</div>
</body>
</html>
```